Business Card Design

Freelance writer, coach, teacher and researcher specialising in improving mathematics teaching and learning in primary schools. I write books and articles for teachers, speak extensively at conferences in UK and aboard. Would like something with a cube in the design. Clean, modern - logo suitable for use on a website. Should NOT look 'childish' (no comic sans or chalkboard type fonts)

Full details to go on card:

Professor Dale Voronin
Building Early Numeracy

info@dalevoronin.net
#dalevoronin26
www.dalevoronin.net
+44 7823 608 142

Industry/Entity Type

Teacher

Contact Information for Business Card

Professor Dale Voronin
Building Early Numeracy

```html
<!DOCTYPE html>
<html lang="en">
<head>
<meta charset="utf-8">
<title>Building Early Numeracy – Business Card</title>
<link href="https://fonts.googleapis.com/css2?family=Nunito:wght@300;400;800&display=swap" rel="stylesheet">
<style>
  :root {
    --backdrop: #b9c3c4;
    --card: #ffffff;
    --orange: #f5a02a;
    --navy: #2e3a8c;
    --grey: #6b6b6b;
  }
  html, body {
    margin: 0;
    width: 1200px;
    height: 1000px;
    overflow: hidden;
    background: var(--backdrop);
    font-family: "Nunito", sans-serif;
  }
  .card {
    position: absolute;
    left: 270px;
    top: 170px;
    width: 660px;
    height: 660px;
    background: var(--card);
    box-shadow: 0 6px 24px rgba(0,0,0,0.12);
  }
  .brand-mark {
    position: absolute;
    left: 70px;
    top: 120px;
    width: 210px;
    height: 210px;
  }
  .wordmark {
    position: absolute;
    right: 60px;
    top: 150px;
    margin: 0;
    text-align: right;
    font-weight: 800;
    font-size: 50px;
    line-height: 0.98;
    letter-spacing: -1px;
    color: var(--navy);
  }
  .details {
    position: absolute;
    right: 60px;
    top: 340px;
    text-align: right;
    color: var(--grey);
  }
  .details .name {
    margin: 0 0 34px;
    font-weight: 800;
    font-size: 27px;
  }
  .details .contact {
    margin: 0;
    font-weight: 300;
    font-size: 24px;
    line-height: 1.28;
  }
</style>
</head>
<body>
  <div class="card">
    <svg class="brand-mark" viewBox="0 0 210 210" aria-hidden="true">
      <circle cx="105" cy="105" r="100" fill="var(--orange)"/>
    </svg>
    <h1 class="wordmark">Building<br>Early<br>Numeracy</h1>
    <div class="details">
      <p class="name">Professor Dale Voronin</p>
      <p class="contact">info@dalevoronin.net<br>#dalevoronin26<br>www.dalevoronin.net<br>+44 7823 608 142</p>
    </div>
  </div>
</body>
</html>
```